Business cards - Yoga Instructor
Quiet Fern Yoga
Creative Brief
Use same font as used in my logo
Use fonts that you feel work well with the logo and style of card
Bright & Fun-filled
Miriam Tovbrask
Certified Yoga Instructor
Austin, Texas
mtovbrask@brightpost.example
www.Quietfern.example
The front should include the "Quiett Fern Yoga" logo that we have uploaded. Also - we would like to include "Offering Veyolin based yoga" on the card as well. perhaps just below the title "Certified Yoga Instructor"
we would like to have the "Ohm" symbol on the back of the card and the words "Strength - Stability - Freedom". here is a link for a sample of the symbol. http://www.breathwheelsite.example/ok.htm We are thinking the Ohm symbol can fill the entire back (even going off the edges) and the text on top.

```html
<!DOCTYPE html>
<html lang="en">
<head>
<meta charset="utf-8">
<title>Quiet Fern Yoga – Business Cards</title>
<link rel="stylesheet" href="https://fonts.googleapis.com/css2?family=Roboto:wght@300;400;700&display=swap">
<style>
  :root {
    --backdrop: #ece8e3;
    --card: #ffffff;
    --ink: #1f1f1f;
    --ink-soft: #3a3a3a;
    --plum: #9a2a8e;
    --violet: #7a4f9c;
    --lilac: #d9b9dd;
    --wave-blue: #a9b3dc;
    --wave-pink: #efc3d8;
  }
  * { margin: 0; padding: 0; box-sizing: border-box; }
  html, body { width: 1200px; height: 926px; overflow: hidden; }
  body {
    background: var(--backdrop);
    font-family: "Roboto", Arial, sans-serif;
    position: relative;
  }
  .card {
    position: absolute;
    width: 736px;
    height: 420px;
    background: var(--card);
    overflow: hidden;
    box-shadow: 0 6px 14px rgba(0,0,0,0.18);
  }
  .card-front { left: 50px; top: 55px; z-index: 1; }
  .card-back { left: 414px; top: 478px; z-index: 2; }
  .waves { position: absolute; inset: 0; width: 100%; height: 100%; }

  .identity {
    position: absolute;
    right: 30px;
    top: 28px;
    text-align: right;
  }
  .identity-name { font-weight: 700; font-size: 27px; color: var(--ink); }
  .identity-title { font-weight: 300; font-size: 18px; color: var(--ink-soft); margin-top: 4px; }
  .identity-offer { font-style: italic; font-size: 17px; color: var(--plum); margin-top: 6px; }

  .brand {
    position: absolute;
    left: 30px;
    top: 252px;
    display: flex;
    align-items: center;
    gap: 14px;
  }
  .brand-dot { width: 22px; height: 22px; border-radius: 50%; background: var(--wave-pink); }
  .brand-name { font-size: 36px; font-weight: 300; color: var(--violet); letter-spacing: 1px; }

  .contact {
    position: absolute;
    right: 30px;
    top: 278px;
    text-align: right;
    font-size: 17px;
    line-height: 25px;
    color: var(--ink-soft);
  }

  .tagline {
    position: absolute;
    left: 30px;
    top: 32px;
    font-size: 29px;
    color: var(--plum);
  }
  .symbol-area {
    position: absolute;
    left: 412px;
    top: 112px;
    width: 214px;
    height: 240px;
    border-radius: 40%;
    background: radial-gradient(circle at 50% 55%, var(--lilac), rgba(217,185,221,0.55));
  }
</style>
</head>
<body>
  <section class="card card-front" aria-label="Business card front">
    <svg class="waves" viewBox="0 0 736 420" aria-hidden="true">
      <path d="M0 10 C180 20 300 200 736 170 L736 185 C300 220 180 40 0 22 Z" fill="var(--wave-pink)" opacity="0.8"/>
      <path d="M60 0 C240 30 380 215 736 195 L736 202 C380 228 240 45 60 0 Z" fill="var(--wave-blue)" opacity="0.9"/>
      <path d="M0 340 C200 330 380 290 736 235 L736 250 C380 305 200 350 0 360 Z" fill="var(--wave-blue)" opacity="0.85"/>
      <path d="M0 372 C220 350 420 300 736 270 L736 278 C420 312 220 362 0 382 Z" fill="var(--wave-pink)" opacity="0.8"/>
    </svg>
    <div class="identity">
      <div class="identity-name">Miriam Tovbrask</div>
      <div class="identity-title">Certified Yoga Instructor</div>
      <div class="identity-offer">"Offering Veyolin based yoga"</div>
    </div>
    <div class="brand">
      <span class="brand-dot"></span>
      <span class="brand-name">Quiet Fern Yoga</span>
    </div>
    <div class="contact">
      <div>Austin, Texas</div>
      <div>(512)-555-0148</div>
      <div>mtovbrask@brightpost.example</div>
      <div>www.Quietfern.example</div>
    </div>
  </section>

  <section class="card card-back" aria-label="Business card back">
    <svg class="waves" viewBox="0 0 736 420" aria-hidden="true">
      <path d="M0 200 C200 230 420 170 736 20 L736 40 C420 190 200 250 0 222 Z" fill="var(--wave-pink)" opacity="0.75"/>
      <path d="M0 220 C260 250 460 200 736 70 L736 78 C460 212 260 262 0 232 Z" fill="var(--wave-blue)" opacity="0.9"/>
      <path d="M0 300 C250 330 470 370 736 300 L736 316 C470 388 250 350 0 318 Z" fill="var(--wave-blue)" opacity="0.75"/>
    </svg>
    <div class="tagline">Strength - Stability - Freedom</div>
    <div class="symbol-area" role="img" aria-label="Large lilac Om symbol"></div>
  </section>
</body>
</html>
```